"Global Leadership & Talent Development Firm" needs a website upgrade

Website Design Project is intended to find a vendor to update and provide maintenance for my website: www.Brightpath7Gains.com. I am looking for a vendor who is an expert with WordPress and eCommerce plugin.

Website Requirements
www.Brightpath7Gains.com

• Media Library (review)- Add video/utube
• Others (plug-ins)
1) eCommerce ability
a) Must have the ability to charge for the eLearning courses
i) Handle credit card processing
ii) Ability to handle yearly subscriptions
iii) Ability to process credits/refunds

Website Updates Assessment Page:
• Totally MORV- Distributor Information
• 4 Crew Patterns Assessment & logo
• Steering Quest- 360 Assessment
• Emotional Intelligence Assessment
Home & Tool Pages:
• K7V License and certification
• PulseCore Trainer
• 4 Crew Patterns training
Client & Contact Pages
• Update Client list
• Update testimonials
Speaker Page Update
Website Add on E-Commerce to sell products
• K7V Certification Program
• PulseCore tools & technology
• Totally MoRV Assessment Distributor
• 4 Crew Pattern Distributor

See attached document describing the updates.

Target Market(s)

Small-Large Business and Corporations
Public Sector Organizations

Industry/Entity Type

Leadership

Number of Pages Required

5+ page

Font styles to use
Other font styles liked:
• www.brightpath7gains.com

Requirements
Must have
• Wordpress expertise
• E-Commerce plugin expertise
• Website Maintenance capability
Nice to have
• Easy access to transfer documents and get feedback/suggestions on the best wording for presenting the information onto my site for each of the pages
Should not have
• Focus on changing the current design of my site

```html
<!DOCTYPE html>
<html lang="en">
<head>
<meta charset="utf-8">
<title>Brightpath7Gains – Developing Leadership Talent &amp; Succession</title>
<link rel="stylesheet" href="https://fonts.googleapis.com/css2?family=Arimo:wght@400;700&display=swap">
<style>
:root{
  --orange:#f0962a;
  --ink:#231f20;
  --text:#2b2b2b;
  --grey-band:#e4e4ea;
  --card:#ffffff;
  --red:#d2352b;
  --amber:#f2a42e;
  --sky:#7dc8e2;
  --slate:#5a5a5a;
  --footer:#231f20;
  --footer-text:#e6e6e6;
  --hero-dark:#1c2a44;
  --hero-mid:#4a6a94;
  --hero-light:#a9bfd8;
}
*{box-sizing:border-box;margin:0;padding:0}
html,body{width:1200px;height:2185px;overflow:hidden;background:#fff}
body{position:relative;font-family:"Arimo",Arial,sans-serif;color:var(--text)}

/* header */
.brand{position:absolute;left:119px;top:34px;width:340px;height:72px;z-index:2}
.brand-mark{position:absolute;left:0;top:0;width:48px;height:71px;background:var(--orange);border-radius:6px}
.brand-name{position:absolute;left:58px;top:18px;font-size:33px;color:#4a4a4a;line-height:1;letter-spacing:-.5px;white-space:nowrap}
.brand-tagline{position:absolute;left:60px;top:54px;font-size:12px;color:#6b6b6b;white-space:nowrap}

.menu{position:absolute;left:881px;top:46px;width:209px;height:232px;background:#fff;border:2px solid #cfd3da;border-radius:5px;box-shadow:0 2px 6px rgba(0,0,0,.15);overflow:hidden;z-index:10}
.menu-head{height:45px;background:var(--orange);display:flex;align-items:center;padding-left:16px;color:#fff;font-size:12px;font-weight:700;position:relative}
.menu-toggle{position:absolute;right:0;top:0;width:28px;height:45px;background:var(--ink);display:flex;align-items:center;justify-content:center}
.menu-item{height:46px;border-bottom:1px solid #e6e6e6;display:flex;align-items:center;padding-left:16px;font-size:12px;color:#333;white-space:nowrap}
.menu-item:last-child{border-bottom:none}

/* hero */
.hero{position:absolute;left:0;top:139px;width:1200px;height:668px;background:radial-gradient(ellipse at 55% 35%,var(--hero-light) 0%,var(--hero-mid) 40%,var(--hero-dark) 100%)}
.hero-arrow{position:absolute;top:452px}
.hero-card{position:absolute;left:119px;top:224px;width:439px;height:240px;background:var(--ink);border:3px solid #8f98a6;border-radius:4px;z-index:3}
.hero-close{position:absolute;right:12px;top:6px;color:#fff;font-size:16px;font-weight:700}
.hero-title{position:absolute;left:26px;top:22px;font-size:38px;line-height:48px;color:#fff;font-weight:400;white-space:nowrap}
.hero-title strong{font-weight:700}
.hero-cta{position:absolute;left:4px;bottom:6px;width:425px;height:40px;background:var(--orange);color:#fff;font-size:15px;font-weight:700;display:flex;align-items:center;padding-left:24px;gap:14px;white-space:nowrap}

/* approach */
.section-title{position:absolute;left:0;width:1200px;text-align:center;font-size:24px;font-weight:700;color:var(--ink);letter-spacing:.5px}
.section-title span{color:var(--orange)}
.approach-text{position:absolute;left:100px;top:934px;width:1000px;text-align:center;font-size:13px;line-height:24.7px;letter-spacing:.6px;color:#333;white-space:nowrap}

/* tools */
.tools{position:absolute;left:0;top:1139px;width:1200px;height:855px;background:var(--grey-band)}
.tools-notch{position:absolute;left:592px;top:-1px;width:0;height:0;border-left:14px solid transparent;border-right:14px solid transparent;border-top:14px solid #fff}
.tool{position:absolute;left:118px;width:972px;height:139px;background:var(--card);border-radius:6px}
.tool-icon{position:absolute;left:2px;top:2px;width:97px;height:135px;border-radius:5px;border:2px solid #d6d6d6;display:flex;align-items:center;justify-content:center;box-shadow:6px 0 0 #e0e0e6}
.tool-icon.red{background:linear-gradient(#e5574c,var(--red))}
.tool-icon.amber{background:linear-gradient(#f6bd5a,var(--amber))}
.tool-icon.sky{background:linear-gradient(#a6dcee,var(--sky))}
.tool-icon.slate{background:linear-gradient(#7a7a7a,var(--slate))}
.tool-title{position:absolute;left:136px;top:30px;font-size:18px;font-weight:400;letter-spacing:.8px;color:var(--ink);white-space:nowrap}
.tool-body{position:absolute;left:136px;top:57px;font-size:13px;line-height:24.7px;letter-spacing:.6px;color:#333;white-space:nowrap}

/* footer */
.footer{position:absolute;left:0;top:1994px;width:1200px;height:191px;background:var(--footer)}
.footer-nav{position:absolute;top:45px;font-size:17px;color:var(--footer-text);letter-spacing:.6px;white-space:nowrap}
.footer-nav.current{font-weight:700;color:#fff}
.footer-rule{position:absolute;left:140px;top:105px;width:920px;height:1px;background:#3a3637}
.copyright{position:absolute;top:143px;width:1200px;text-align:center;font-size:14px;color:#bdbdbd;letter-spacing:.8px}
.copyright b{color:#e0e0e0}
.contact-pop{position:absolute;left:805px;top:82px;width:285px;height:74px;background:#fff;border-radius:4px;font-size:14px;color:#333;letter-spacing:.6px}
.contact-pop::before{content:"";position:absolute;left:178px;top:-10px;border-left:10px solid transparent;border-right:10px solid transparent;border-bottom:10px solid #fff}
.contact-line{position:absolute;right:18px;display:flex;align-items:center;gap:8px;white-space:nowrap}
</style>
</head>
<body>

<section class="hero" role="img" aria-label="Photo of a businessman facing a glowing wall of sketched business ideas and diagrams"></section>
<svg class="hero-arrow" style="left:40px" width="22" height="40" viewBox="0 0 22 40"><path d="M19 3 4 20l15 17" fill="none" stroke="#fff" stroke-width="3"/></svg>
<svg class="hero-arrow" style="left:1138px" width="22" height="40" viewBox="0 0 22 40"><path d="M3 3l15 17L3 37" fill="none" stroke="#fff" stroke-width="3"/></svg>
<div class="hero-card">
  <div class="hero-close">x</div>
  <h1 class="hero-title">Behind every<br>good result is a<br><strong>great insight.</strong></h1>
  <div class="hero-cta">Learn More about Developing Leadership Talent <span>›</span></div>
</div>

<header>
  <div class="brand">
    <div class="brand-mark"></div>
    <div class="brand-name">Brightpath7Gains</div>
    <div class="brand-tagline">Developing Leadership Talent &amp; Succession</div>
  </div>
  <nav class="menu">
    <div class="menu-head">Menu
      <div class="menu-toggle">
        <svg width="12" height="12" viewBox="0 0 12 12"><rect y="1" width="12" height="2" fill="#fff"/><rect y="5" width="12" height="2" fill="#fff"/><rect y="9" width="12" height="2" fill="#fff"/></svg>
      </div>
    </div>
    <div class="menu-item">Coaching7Gains™</div>
    <div class="menu-item">Managing7Gains™</div>
    <div class="menu-item">Mentoring7Gains™</div>
    <div class="menu-item">Core Outlook Indicator™</div>
  </nav>
</header>

<h2 class="section-title" style="top:864px">Our <span>Approach</span></h2>
<p class="approach-text">Looking for a boxed approach? You won't find it here. Our approach is an exchange; an exchange of dynamic listening and<br>deliberate question asking. We ultimately identify the key leadership and talent factors that influence your organization's<br>issues and successes. Then we apply our breadth of experience in working with companies like yours and people<br>like you to develop a model of your company's leadership culture, language, symbols and values. As partners,<br>we collaborate with you to mold, customize, and implement an application uniquely designed for your<br>people, values, and systems, and strategies.</p>

<section class="tools">
  <div class="tools-notch"></div>
  <h2 class="section-title" style="top:56px">Tools</h2>

  <article class="tool" style="top:126px">
    <div class="tool-icon red">
      <svg width="60" height="60" viewBox="0 0 60 60" fill="#fff"><rect x="4" y="40" width="8" height="16" rx="2"/><rect x="17" y="34" width="8" height="22" rx="2"/><rect x="30" y="26" width="8" height="30" rx="2"/><rect x="43" y="16" width="8" height="40" rx="2"/><path d="M47 2l9 11h-18z"/></svg>
    </div>
    <h3 class="tool-title">Coaching7Gains™</h3>
    <p class="tool-body">Most leaders believe that setting ambitious goals and merely providing regular corrective feedback will<br>create the results they need. Research and experience prove that this is NOT enough.</p>
  </article>

  <article class="tool" style="top:300px">
    <div class="tool-icon amber">
      <svg width="70" height="66" viewBox="0 0 70 66" fill="#fff"><path d="M35 2l5 10 11 1.5-8 7.5 2 11-10-5.5-10 5.5 2-11-8-7.5 11-1.5z"/><path d="M17 32l5 10 11 1.5-8 7.5 2 11-10-5.5-10 5.5 2-11-8-7.5 11-1.5z"/><path d="M53 32l5 10 11 1.5-8 7.5 2 11-10-5.5-10 5.5 2-11-8-7.5 11-1.5z"/></svg>
    </div>
    <h3 class="tool-title">Managing7Gains™</h3>
    <p class="tool-body">Management training must equip and empower managers to drive better results, make better decisions,<br>and develop strong performers and teams. Enter Managing7Gains™, an intuitive and practical<br>management model for managers and trainers.</p>
  </article>

  <article class="tool" style="top:477px">
    <div class="tool-icon sky">
      <svg width="66" height="50" viewBox="0 0 66 50" fill="#fff"><circle cx="14" cy="14" r="8"/><circle cx="52" cy="14" r="8"/><path d="M0 40c0-10 6-16 14-16s14 6 14 16z"/><path d="M38 40c0-10 6-16 14-16s14 6 14 16z"/><circle cx="33" cy="18" r="10"/><path d="M15 50c0-13 8-20 18-20s18 7 18 20z"/></svg>
    </div>
    <h3 class="tool-title">Mentoring7Gains™</h3>
    <p class="tool-body">Research shows that employees entering the workplace today want work to afford them the opportunity<br>to make new friends, learn new skills and connect to a larger purpose. That sense of purpose is a key<br>factor in their job satisfaction and mentoring programs offer a vehicle to discover and confirm the purpose.</p>
  </article>

  <article class="tool" style="top:653px">
    <div class="tool-icon slate">
      <svg width="64" height="64" viewBox="0 0 64 64" fill="#fff"><path d="M32 2l10 12h-6v14h14v-6l12 10-12 10v-6H36v14h6L32 62 22 50h6V36H14v6L2 32l12-10v6h14V14h-6z"/></svg>
    </div>
    <h3 class="tool-title">Core Outlook Indicator®</h3>
    <p class="tool-body">Achieving results is about closing gaps and turning strategy into execution and creativity into innovation.<br>The bridge over these gaps is Collaboration. And the columns of this bridge are mind sets.</p>
  </article>
</section>

<footer class="footer">
  <a class="footer-nav current" style="left:148px">Home</a>
  <a class="footer-nav" style="left:232px">Approach</a>
  <a class="footer-nav" style="left:346px">Tools</a>
  <a class="footer-nav" style="left:424px">Assessments</a>
  <a class="footer-nav" style="left:570px">Clients</a>
  <a class="footer-nav" style="left:663px">Consultants</a>
  <a class="footer-nav" style="left:799px">Speaking</a>
  <a class="footer-nav" style="left:912px">Blog</a>
  <a class="footer-nav" style="left:984px">Contact</a>
  <div class="footer-rule"></div>
  <div class="contact-pop">
    <div class="contact-line" style="top:15px">
      <svg width="16" height="12" viewBox="0 0 16 12"><rect x=".5" y=".5" width="15" height="11" fill="#333"/><path d="M1 1l7 6 7-6" fill="none" stroke="#fff" stroke-width="1.4"/></svg>
      Dana@Brightpath7Gains.com
    </div>
    <div class="contact-line" style="top:44px">
      <svg width="12" height="16" viewBox="0 0 12 16"><rect width="12" height="16" rx="1.5" fill="#333"/><rect x="2" y="2" width="8" height="10" fill="#fff"/></svg>
      (555) <b>014-2271</b>
    </div>
  </div>
  <p class="copyright">© <b>Brightpath7Gains</b>. All Rights Reserved</p>
</footer>

</body>
</html>
```